Outdoor Company Business Card design

We are an outdoor adventure company needing a business card. We sell outdoor adventures and clothing. Please use our logo in the business card. We are looking for something unique but delivers a clear message as to who we are. Please be creative

Target Market(s)

Outdoor adventures

Industry/Entity Type

Business

Contact Information for Business Card

Business name: TrailBirch If using the logo, no need to have a spot for the name
Owner / CEO: Ross Dalby
Website: TrailBirch.example
Facebook: Pagebook.example/TrailBirch
Instagram: @dalby_ross
phone number: 555-304-7192
Email: Dalbycrew@TrailBirch.example

Colors

Designer to choose colors to be used in the design.

Requirements
Must have
• The business card must include the details mentioned above. ie logo, my name, email, facebook, instagram, website, and phone number.
Should not have
• should not be cluttered or look messy

```html
<!DOCTYPE html>
<html lang="en">
<head>
<meta charset="utf-8">
<title>TrailBirch Business Card</title>
<link rel="stylesheet" href="https://fonts.googleapis.com/css2?family=Lato:wght@400;700;900&display=swap">
<style>
  :root {
    --orange: #f15a29;
    --blue: #1d72bb;
    --grey: #9a9b9d;
    --ink: #3a3a3a;
    --white: #ffffff;
    --backdrop: #e9e7e4;
  }
  * { margin: 0; padding: 0; box-sizing: border-box; }
  html, body { width: 1200px; height: 900px; overflow: hidden; }
  body {
    background: var(--backdrop);
    font-family: "Lato", sans-serif;
    position: relative;
  }
  .card {
    position: absolute;
    box-shadow: 0 6px 18px rgba(0,0,0,.18);
    overflow: hidden;
  }
  /* Front */
  .card-front {
    left: 78px; top: 34px; width: 588px; height: 364px;
    background: var(--white);
  }
  .front-sweep { position: absolute; left: 0; top: 0; width: 588px; height: 170px; }
  .brand-name {
    position: absolute; left: 228px; top: 194px; width: 340px;
    text-align: center;
    font-weight: 900; font-size: 44px; letter-spacing: 3px;
    text-transform: uppercase; color: var(--blue); line-height: 1;
    white-space: nowrap;
  }
  .owner { position: absolute; left: 30px; top: 188px; }
  .owner-name {
    font-size: 20px; font-weight: 400; letter-spacing: .5px;
    color: var(--blue); text-transform: uppercase; line-height: 1.1;
  }
  .owner-name .surname { color: var(--orange); }
  .owner-role { font-size: 17px; color: var(--ink); margin-top: 3px; }
  .contacts { position: absolute; left: 30px; top: 270px; list-style: none; }
  .contacts li {
    display: flex; align-items: center; gap: 6px;
    font-size: 16.5px; color: var(--ink); height: 22px;
  }
  .contacts svg { width: 12px; height: 12px; fill: var(--blue); flex: none; }
  /* Back */
  .card-back {
    left: 388px; top: 505px; width: 567px; height: 352px;
    background: linear-gradient(180deg, var(--orange) 0%, #c98a78 35%, #8da1b6 60%, #2f7cc0 100%);
    color: var(--white);
  }
  .back-brand {
    position: absolute; left: 0; right: 0; top: 184px;
    text-align: center; font-weight: 900; font-size: 48px;
    letter-spacing: 5px; text-transform: uppercase; line-height: 1;
    white-space: nowrap;
  }
  .back-rule {
    position: absolute; left: 107px; width: 350px; top: 260px;
    border-top: 1px solid rgba(255,255,255,.7);
  }
  .socials {
    position: absolute; left: 0; right: 0; top: 280px;
    display: flex; justify-content: center; gap: 10px;
    font-size: 16px; white-space: nowrap;
  }
  .socials span { display: flex; align-items: center; gap: 4px; }
  .socials i {
    display: inline-block; width: 16px; height: 16px;
    background: var(--white); border-radius: 2px;
  }
</style>
</head>
<body>
  <section class="card card-front">
    <svg class="front-sweep" viewBox="0 0 588 170" role="img" aria-label="Grey bird in flight with sweeping wings over an orange and blue band">
      <defs>
        <linearGradient id="sweepTone" x1="0" y1="0" x2="1" y2="0">
          <stop offset="0" stop-color="#f15a29"/>
          <stop offset=".45" stop-color="#9a9b9d"/>
          <stop offset="1" stop-color="#1d72bb"/>
        </linearGradient>
      </defs>
      <path d="M0 0 H588 V120 C520 95 470 70 400 62 C320 55 250 80 180 110 C120 135 60 130 0 128 Z" fill="url(#sweepTone)"/>
    </svg>
    <div class="brand-name">TrailBirch</div>
    <div class="owner">
      <p class="owner-name">Ross <span class="surname">Dalby</span></p>
      <p class="owner-role">Owner / CEO</p>
    </div>
    <ul class="contacts">
      <li><svg viewBox="0 0 12 12"><path d="M2 1h2l1 3-1.5 1a6 6 0 0 0 3.5 3.5L8 7l3 1v2a1 1 0 0 1-1 1A9 9 0 0 1 1 2a1 1 0 0 1 1-1z"/></svg>555-304-7192</li>
      <li><svg viewBox="0 0 12 12"><path d="M0 2h12v8H0z"/><path d="M1 3l5 4 5-4" fill="none" stroke="#fff" stroke-width="1"/></svg>Dalbycrew@TrailBirch.example</li>
      <li><svg viewBox="0 0 12 12"><circle cx="6" cy="6" r="5.5"/></svg>www.TrailBirch.example</li>
    </ul>
  </section>

  <section class="card card-back">
    <div class="back-brand">TrailBirch</div>
    <div class="back-rule"></div>
    <div class="socials">
      <span><i></i>Pagebook.example/TrailBirch</span>
      <span><i></i>@dalby_ross</span>
    </div>
  </section>
</body>
</html>
```